high-impact, conversion-focused website redesign for the government sector

Objective: To design and develop a high-impact, conversion-focused digital platform that solidifies Harrowgate Lumen Advisors (HLA) as the leading communications and strategy firm for government, defense, and industrial clients. The site must project authority, innovation, and sophisticated precision. See the creative breif for more information

Target Market(s)

Government contractors

Industry/Entity Type

Government, defense, industrials

Coding

Coded - Design and coding required

Number of Pages Required

5+ page

Font styles to use
Other font styles liked:
• See the current website

Requirements
Must have
• See design brief
Nice to have
• See design brief
Should not have
• See design brief

```html
<!DOCTYPE html>
<html lang="en">
<head>
<meta charset="utf-8">
<title>Harrowgate Lumen Advisors — Get in Touch</title>
<link rel="stylesheet" href="https://fonts.googleapis.com/css2?family=Nunito:wght@400;600;700;800&display=swap">
<style>
:root{
  --ink:#000000;
  --navy:#0c2b48;
  --field:#ffffff;
  --placeholder:#6b6b6b;
  --green:#7cc242;
  --white:#ffffff;
  --rule:#2a2a2a;
  --hero-a:#0b1a2c;
  --hero-b:#1f4f7a;
  --hero-c:#6fa6d4;
}
*{box-sizing:border-box;margin:0;padding:0}
html,body{width:1200px;height:1115px;overflow:hidden}
body{font-family:"Nunito",sans-serif;background:var(--ink);color:var(--white);position:relative}
.hero{position:absolute;left:0;top:0;width:1200px;height:715px;
  background:radial-gradient(ellipse at 20% 30%,var(--hero-c) 0%,transparent 45%),
             radial-gradient(ellipse at 85% 35%,#4f86b8 0%,transparent 40%),
             linear-gradient(180deg,var(--hero-b) 0%,var(--hero-a) 100%);}
.hero-title{position:absolute;top:104px;left:0;width:1200px;text-align:center;
  font-size:38px;font-weight:800;color:var(--ink);letter-spacing:.5px}
.contact-form{position:absolute;left:239px;top:184px;width:722px;height:414px;
  background:var(--navy);border-radius:9px}
.field{position:absolute;width:329px;height:46px;background:var(--field);border-radius:8px;
  padding:0 14px;display:flex;align-items:center;font-size:13.5px;color:var(--placeholder)}
.field.left{left:27px}.field.right{left:366px}
.field.message{left:27px;width:668px;height:74px;align-items:flex-start;padding-top:14px}
.submit{position:absolute;left:291px;top:345px;width:140px;height:38px;border-radius:8px;
  background:var(--green);color:var(--white);font-weight:700;font-size:13px;
  display:flex;align-items:center;justify-content:center}
.brand{position:absolute;left:52px;top:790px;display:flex;align-items:center;gap:10px}
.brand-mark{width:20px;height:20px;background:var(--green)}
.brand-name{font-size:21px;font-weight:700;color:var(--white);line-height:1.15}
.social{position:absolute;left:52px;top:888px;display:flex;gap:12px}
.social span{width:22px;height:22px;border:2px solid var(--green);border-radius:50%}
.col{position:absolute;top:764px}
.col h3{font-size:15px;font-weight:800;letter-spacing:.2px;margin-bottom:6px}
.col li{list-style:none;font-size:13.5px;height:32.8px}
.col.nav{left:427px}.col.services{left:614px}.col.contact{left:895px}
.contact-row{display:flex;gap:10px;font-size:13.5px;line-height:18px;margin-bottom:15px}
.contact-row svg{flex:none;margin-top:1px}
.rule{position:absolute;left:0;top:1057px;width:1200px;height:1px;background:var(--rule)}
.copyright{position:absolute;top:1071px;left:0;width:1196px;text-align:center;font-size:11.5px}
</style>
</head>
<body>
<section class="hero" role="img" aria-label="Photograph of an operations control room with large wall maps and analysts at monitors">
</section>
<h1 class="hero-title">GET IN TOUCH</h1>

<form class="contact-form" aria-label="Contact form">
  <div class="field left" style="top:41px">Frst Name*</div>
  <div class="field right" style="top:41px">Last Name*</div>
  <div class="field left" style="top:106px">Company Name</div>
  <div class="field right" style="top:106px">Phone*</div>
  <div class="field left" style="top:170px">Website U R L*</div>
  <div class="field right" style="top:170px">Phone*</div>
  <div class="field message" style="top:235px">Please tell us more about you we can help</div>
  <div class="submit">SUBMIT NOW</div>
</form>

<footer>
  <div class="brand">
    <span class="brand-mark"></span>
    <span class="brand-name">Harrowgate Lumen<br>Advisors</span>
  </div>
  <div class="social" aria-label="Social links"><span></span><span></span><span></span></div>

  <div class="col nav">
    <h3>NAVIGATION</h3>
    <ul><li>Home</li><li>Advisory</li><li>Services</li><li>About Us</li><li>Blog</li><li>Contact Us</li></ul>
  </div>
  <div class="col services">
    <h3>SERVICES</h3>
    <ul><li>Corporate Communications</li><li>Public Relations</li><li>Government Affairs</li><li>Crisis Communications</li><li>Digital Marketing</li><li>Strategic Connections</li><li>Investor Relations</li><li>Event Management</li></ul>
  </div>
  <div class="col contact">
    <h3>CONTACT US</h3>
    <div class="contact-row">
      <svg width="18" height="22" viewBox="0 0 18 22"><path d="M9 0C4 0 0 4 0 9c0 6 9 13 9 13s9-7 9-13c0-5-4-9-9-9z" fill="#7cc242"/><circle cx="9" cy="9" r="3.2" fill="#000"/></svg>
      <span>Larkfield Regional Airfield<br>Hangar 4, PO Box 41870<br>Larkfield, NL A2B 7C9 Canada</span>
    </div>
    <div class="contact-row">
      <svg width="18" height="18" viewBox="0 0 24 24"><path d="M6.6 10.8a15 15 0 006.6 6.6l2.2-2.2a1 1 0 011-.25 11.4 11.4 0 003.6.57 1 1 0 011 1V20a1 1 0 01-1 1A17 17 0 013 4a1 1 0 011-1h3.5a1 1 0 011 1c0 1.25.2 2.45.57 3.57a1 1 0 01-.25 1z" fill="#7cc242"/></svg>
      <span>0248173905612</span>
    </div>
    <div class="contact-row">
      <svg width="18" height="14" viewBox="0 0 18 14"><rect width="18" height="14" fill="#7cc242"/><path d="M1 1l8 7 8-7M1 13l6-5M17 13l-6-5" stroke="#000" stroke-width="1.4" fill="none"/></svg>
      <span>info@harrowgatelumen.com</span>
    </div>
  </div>

  <div class="rule"></div>
  <p class="copyright">2025 COPYRIGHT HARROWGATE LUMEN</p>
</footer>
</body>
</html>
```